Torvane Center for Restorative Medicine

I need a full informational website for my medical practice. I would like to use my logo and also include a lot of emblems/pictures (also a picture of me in a white coat). The website should have a function for people to inquire and send me messages. I will be offering needle-less regenerative injection therapy, stem cell treatments, bioidentical hormone therapy, treatment for chronic illness, neurodegenerative diseases, skin rejuvenation, hair restoration, male enhancement, female enhancement, and anti-aging. The practice will not be accepting insurance and will be cash/credit card only.
A good example of written content and functionality is this website:
http://thebqvx.example/. However, I want different theme and tones.
Target Market(s)
High end clientele in Los Angeles, Southern California. Health minded people who are interested in living better and longer and can afford anti-aging treatments. Men and women who want to improve sexual health and wellbeing.
Industry/Entity Type
Medical And Science
Coding
Coded - Design and coding required
Number of Pages Required
5+ page
Font styles to use
Requirements
Must have
- 1. I will need to be able to move the site to other servers (needed for site speed)
- 2. Site must be build on WordPress
- 3. Full admin credentials for domain, cpanel, wordpress, ftp.
- 4. No third party interaction on development and content deployment once the site is on different servers
- 5. I will need the ability to add content and links to the site
- 6. I will need the ability to optimize the site for speed
- 7. I will need to ability to modify URLs so they are more SEO friendly
Nice to have
- pictures of stem cells, health improvement and regeneration, beauty, youthful individuals, older healthy and happy individuals. Medical designs.
Should not have
- flowers, dna

```html
<!DOCTYPE html>
<html lang="en">
<head>
<meta charset="utf-8">
<title>Torvane Center for Restorative Medicine</title>
<link rel="stylesheet" href="https://fonts.googleapis.com/css2?family=Lato:wght@400;700&family=Marcellus&display=swap">
<style>
:root{
  --navy:#0c2878;
  --navy-deep:#0a2266;
  --ink:#0a0a0a;
  --night:#0b0c1e;
  --green:#1fae85;
  --white:#ffffff;
  --text:#333333;
  --muted:#555555;
  --field:#eeeeee;
  --field-line:#cfcfcf;
  --serif:"Marcellus", Georgia, serif;
  --sans:"Lato", Arial, sans-serif;
}
*{box-sizing:border-box;margin:0;padding:0}
html,body{width:1200px;height:3448px;overflow:hidden}
body{position:relative;background:var(--white);font-family:var(--sans);color:var(--text)}
.abs{position:absolute}

/* top navigation */
.topnav{left:0;top:0;width:1200px;height:50px;background:var(--ink);display:flex;justify-content:center;align-items:center;gap:0}
.topnav a{color:var(--white);text-decoration:none;font-size:15px;letter-spacing:.5px;padding:0 24px;position:relative;line-height:50px}
.topnav a.active::after{content:"";position:absolute;left:18px;right:18px;bottom:0;height:3px;background:var(--white)}
.topnav .dot{width:8px;height:8px;border-radius:50%;background:var(--white)}

/* header */
.header{left:0;top:50px;width:1200px;height:106px;background:var(--navy-deep)}
.brand{left:80px;top:20px;display:flex;align-items:center;gap:14px;color:var(--white)}
.brand-mark{width:60px;height:60px;border-radius:50%;background:var(--white)}
.brand-name{font-family:var(--serif);font-size:40px;line-height:1;letter-spacing:1px}
.brand-tag{font-family:var(--serif);font-size:11px;letter-spacing:.5px;margin-top:4px}
.contact-chip{top:25px;display:flex;align-items:center;gap:22px;color:var(--white)}
.contact-chip .icon{width:56px;height:56px;border:1.5px solid var(--white);display:flex;align-items:center;justify-content:center}
.contact-chip .label{font-size:15px;letter-spacing:.5px}
.contact-chip .value{font-size:19px;font-weight:700;margin-top:4px}
.contact-chip .value.small{font-size:16px;font-weight:400}

/* hero */
.hero{left:0;top:156px;width:1200px;height:598px;background:var(--navy);clip-path:polygon(0 0,1200px 0,1200px 476px,667px 598px,0 494px)}
.hero-figure{left:632px;top:16px;width:426px;height:560px;background:radial-gradient(ellipse at 50% 45%,#2fb894 0%,#1f8f86 35%,rgba(12,40,120,0) 70%)}
.hero-title{left:80px;top:152px;font-family:var(--serif);font-size:44px;line-height:1.15;color:var(--white);letter-spacing:.5px}
.hero-text{left:80px;top:278px;width:560px;font-size:18px;line-height:1.6;color:var(--white)}
.hero-arrow{top:212px}

/* welcome */
.welcome-photo{left:0;top:650px;width:690px;height:548px;background:linear-gradient(90deg,#b8c4cc 0%,#d7dde0 45%,#eef0ee 75%,#ffffff 100%)}
.welcome-title{left:660px;top:842px;font-family:var(--serif);font-size:40px;color:#1a1a1a;letter-spacing:1px}
.welcome-copy{left:660px;top:904px;width:440px;font-size:13.5px;line-height:1.75;color:var(--muted)}
.welcome-copy p+p{margin-top:10px}
.btn{background:var(--green);color:var(--white);font-family:var(--serif);font-size:19px;letter-spacing:1px;display:flex;align-items:center;justify-content:center;height:46px}

/* services */
.services{left:0;top:1198px;width:1200px;height:779px;background:radial-gradient(ellipse at 50% 50%,#1d2b48 0%,#0d1126 55%,var(--night) 100%)}
.services-title{left:0;top:50px;width:1200px;text-align:center;font-family:var(--serif);font-size:42px;color:var(--white);letter-spacing:1px}
.services-intro{left:300px;top:110px;width:600px;text-align:center;font-size:13.5px;line-height:1.7;color:var(--white)}
.doctor-photo{left:437px;top:209px;width:333px;height:570px;background:linear-gradient(180deg,#3a2a26 0%,#c9b4a4 22%,#f1f3f6 45%,#e4e8ee 100%);border-radius:160px 160px 0 0}
.service{display:flex;align-items:center;gap:22px;color:var(--white);font-size:15px;line-height:1.45}
.service .box{width:62px;height:62px;background:#707480;border-radius:6px;display:flex;align-items:center;justify-content:center;flex:none}
.service.left{right:844px;text-align:right}
.service.right{left:839px}

/* testimonials */
.testi-title{left:0;top:2024px;width:1200px;text-align:center;font-family:var(--serif);font-size:42px;color:#1a1a1a;letter-spacing:1px}
.testi-band{left:0;top:2260px;width:1200px;height:308px;background:var(--green);clip-path:polygon(0 0,600px 92px,1200px 0,1200px 223px,600px 308px,0 223px)}
.testi-avatar{left:506px;top:2115px;width:188px;height:188px;border-radius:50%;background:linear-gradient(160deg,#d9d4cf,#9c8f86);border:5px solid #e6e6e6}
.testi-quote{left:230px;top:2400px;width:740px;text-align:center;color:var(--white);font-size:13.5px;line-height:1.9}
.testi-name{left:0;top:2494px;width:1200px;text-align:center;color:var(--white);font-size:14px;letter-spacing:.5px}

/* contact */
.help{left:0;top:2650px;width:1200px;text-align:center;font-size:22px;color:#333;letter-spacing:.5px}
.help-phone{left:0;top:2682px;width:1200px;text-align:center;font-size:46px;font-weight:700;color:var(--navy)}
.field{background:var(--field);border:1px solid var(--field-line);font-size:14px;color:#555;padding:0 14px;display:flex;align-items:center}
.field.message{align-items:flex-start;padding-top:16px}
.submit{left:439px;top:3002px;width:322px;height:51px}
.pin{left:580px;top:3124px}
.address{left:400px;top:3200px;width:400px;text-align:center;font-size:18px;line-height:1.65;color:#666}

/* footer */
.footer{left:0;top:3322px;width:1200px;height:126px;background:var(--ink);color:var(--white)}
.footer-links{left:0;top:30px;width:1200px;display:flex;justify-content:center;font-size:14px}
.footer-links span{padding:0 18px;border-left:1px solid var(--white)}
.footer-links span:first-child{border-left:none}
.footer-copy{left:0;top:84px;width:1200px;text-align:center;font-size:13px}
</style>
</head>
<body>

<nav class="abs topnav">
  <a class="active">HOME</a><span class="dot"></span>
  <a>ABOUT</a><span class="dot"></span>
  <a>SERVICES</a><span class="dot"></span>
  <a>DR.BIO</a><span class="dot"></span>
  <a>TESTIMONIALS</a><span class="dot"></span>
  <a>CONTACT</a>
</nav>

<header class="abs header">
  <div class="abs brand">
    <span class="brand-mark"></span>
    <div>
      <div class="brand-name">Torvane</div>
      <div class="brand-tag">Center for Restorative Medicine</div>
    </div>
  </div>
  <div class="abs contact-chip" style="left:676px">
    <span class="icon"><svg width="26" height="26" viewBox="0 0 24 24" fill="none" stroke="#fff" stroke-width="1.6"><path d="M5 3h4l2 5-2.5 1.5a11 11 0 0 0 6 6L16 13l5 2v4a2 2 0 0 1-2 2A17 17 0 0 1 3 5a2 2 0 0 1 2-2z"/></svg></span>
    <div><div class="label">CALL US NOW</div><div class="value">123 456 7890</div></div>
  </div>
  <div class="abs contact-chip" style="left:936px">
    <span class="icon"><svg width="26" height="26" viewBox="0 0 24 24" fill="none" stroke="#fff" stroke-width="1.6"><rect x="3" y="5" width="18" height="14"/><path d="M3 5l9 8 9-8"/></svg></span>
    <div><div class="label">EMAIL US</div><div class="value small">info@torvane.example</div></div>
  </div>
</header>

<section class="abs welcome-photo" role="img" aria-label="Photo of a smiling older couple walking by the sea"></section>

<section class="abs hero">
  <div class="abs hero-figure" role="img" aria-label="Illustration of a human figure formed from glowing green particles"></div>
  <h1 class="abs hero-title">CENTER FOR<br>REGENERATIVE MEDICINE</h1>
  <p class="abs hero-text">Lorem Ipsum is simply dummy text of the printing and typesetting industry Lorem Ipsum has been the industry's.</p>
  <svg class="abs hero-arrow" style="left:26px" width="22" height="36" viewBox="0 0 22 36" fill="none" stroke="#fff" stroke-width="4"><path d="M18 3L4 18l14 15"/></svg>
  <svg class="abs hero-arrow" style="left:1150px" width="22" height="36" viewBox="0 0 22 36" fill="none" stroke="#fff" stroke-width="4"><path d="M4 3l14 15L4 33"/></svg>
</section>

<h2 class="abs welcome-title">WELCOME TO TORVANE</h2>
<div class="abs welcome-copy">
  <p>Lorem Ipsum is simply dummy text of the printing and typesetting industry. Lorem Ipsum has been the industry's standard dummy text ever since the 1500s, when an unknown printer took a galley.</p>
  <p>It has survived not only five centuries, but also the leap into electro typesetting, remaining essentially unchanged.</p>
</div>
<a class="abs btn" style="left:657px;top:1062px;width:196px">KNOW MORE</a>
<a class="abs btn" style="left:876px;top:1062px;width:195px">CONTACT US</a>

<section class="abs services">
  <h2 class="abs services-title">SERVICES</h2>
  <p class="abs services-intro">Lorem Ipsum is simply dummy text of the printing and typesetting industry. Lorem Ipsum has been the industry's standard dummy text ever since.</p>
  <div class="abs doctor-photo" role="img" aria-label="Photo of the doctor in a white coat with a stethoscope"></div>

  <div class="abs service left" style="top:215px"><span>male enhancement</span><span class="box"><svg width="32" height="32" viewBox="0 0 24 24" fill="#fff"><circle cx="12" cy="8" r="4"/><path d="M4 21c0-5 4-7 8-7s8 2 8 7z"/></svg></span></div>
  <div class="abs service left" style="top:318px"><span>stem cell treatments</span><span class="box"><svg width="32" height="32" viewBox="0 0 24 24" fill="#fff" stroke="#fff" stroke-width="1.2"><circle cx="6" cy="6" r="2"/><circle cx="18" cy="8" r="2"/><circle cx="12" cy="13" r="2"/><circle cx="7" cy="19" r="2"/><circle cx="18" cy="18" r="2"/><path d="M6 6l6 7 6-5M12 13l-5 6M12 13l6 5" fill="none"/></svg></span></div>
  <div class="abs service left" style="top:422px"><span>bioidentical hormone<br>therapy</span><span class="box"><svg width="32" height="32" viewBox="0 0 24 24" fill="#fff"><path d="M9 3h6v6h6v6h-6v6H9v-6H3V9h6z"/></svg></span></div>
  <div class="abs service left" style="top:525px"><span>treatment for chronic<br>illness</span><span class="box"><svg width="32" height="32" viewBox="0 0 24 24" fill="#fff"><circle cx="12" cy="4" r="2.5"/><path d="M8 8h8v7h-2v7h-4v-7H8z"/></svg></span></div>
  <div class="abs service left" style="top:628px"><span>anti-aging</span><span class="box"><svg width="32" height="32" viewBox="0 0 24 24" fill="none" stroke="#fff" stroke-width="1.6"><ellipse cx="12" cy="12" rx="7" ry="9"/><path d="M9 10h6M10 15h4"/></svg></span></div>

  <div class="abs service right" style="top:215px"><span class="box"><svg width="32" height="32" viewBox="0 0 24 24" fill="none" stroke="#fff" stroke-width="2"><circle cx="12" cy="12" r="9"/><path d="M8 8c4 0 6 3 8 8"/></svg></span><span>skin rejuvenation</span></div>
  <div class="abs service right" style="top:318px"><span class="box"><svg width="32" height="32" viewBox="0 0 24 24" fill="none" stroke="#fff" stroke-width="1.6"><path d="M4 20h16M6 20v-6h12v6M8 14V6M12 14V4M16 14V6"/></svg></span><span>hair restoration</span></div>
  <div class="abs service right" style="top:422px"><span class="box"><svg width="32" height="32" viewBox="0 0 24 24" fill="none" stroke="#fff" stroke-width="1.8"><path d="M20 4l-3 3M17 4l3 3M15 6l3 3-9 9-3-3zM6 15l-3 6 6-3"/></svg></span><span>regenerative injection<br>therapy</span></div>
  <div class="abs service right" style="top:525px"><span class="box"><svg width="32" height="32" viewBox="0 0 24 24" fill="#fff"><path d="M12 21c-6-4-9-7-9-11a4.5 4.5 0 0 1 9-1 4.5 4.5 0 0 1 9 1c0 4-3 7-9 11z"/></svg></span><span>neurodegenerative<br>diseases</span></div>
  <div class="abs service right" style="top:628px"><span class="box"><svg width="32" height="32" viewBox="0 0 24 24" fill="#fff"><circle cx="12" cy="8" r="4"/><path d="M4 21c0-5 4-7 8-7s8 2 8 7z"/></svg></span><span>female enhancement</span></div>
</section>

<h2 class="abs testi-title">TESTIMONIALS</h2>
<div class="abs testi-band"></div>
<div class="abs testi-avatar" role="img" aria-label="Portrait photo of a smiling client"></div>
<p class="abs testi-quote">Lorem Ipsum is simply dummy text of the printing and typesetting industry. Lorem Ipsum has been the industry's standard dummy text ever since the 1500s, when an unknown printer took a galley of type and scrambled it to make a type specimen book. It has survived not only five centuries.</p>
<p class="abs testi-name">-NAME SURNAME</p>

<p class="abs help">NEED HELP? CALL US</p>
<p class="abs help-phone">123 456 7890</p>
<div class="abs field" style="left:76px;top:2772px;width:324px;height:53px">Name</div>
<div class="abs field" style="left:437px;top:2772px;width:324px;height:53px">Email</div>
<div class="abs field" style="left:800px;top:2772px;width:322px;height:53px">Phone</div>
<div class="abs field message" style="left:76px;top:2857px;width:1046px;height:113px">Message</div>
<a class="abs btn submit">SUBMIT MESSAGE</a>
<svg class="abs pin" width="40" height="60" viewBox="0 0 40 60"><path d="M20 2C10 2 3 9.5 3 19c0 12 17 29 17 29s17-17 17-29C37 9.5 30 2 20 2z" fill="none" stroke="#0c2878" stroke-width="5"/><circle cx="20" cy="19" r="6" fill="#0c2878"/><ellipse cx="20" cy="56" rx="10" ry="3" fill="#0c2878"/></svg>
<p class="abs address">Lorem Ipsum is simply dummy text of the printing and typesetting industry.</p>

<footer class="abs footer">
  <div class="abs footer-links"><span>Home</span><span>About</span><span>Services</span><span>Dr.Bio</span><span>Testimonials</span><span>Contact</span></div>
  <p class="abs footer-copy">©Orthopedic Surgeon- 2018. All Rights Reserved.</p>
</footer>

</body>
</html>
```